" PRESTA SERVIÇOS DE TECNOLOGIA (T.I.) COMO: DESENVOLVIMENTO E IMPLANTAÇAO DE SISTEMAS, ERP, HELPDESK, HOST, CLOUD... EXCLUSIVAMENTE NO SEGMENTO DE SAUDE (HOSPITAIS E CLINICAS) "

```html
<!DOCTYPE html>
<html lang="pt-BR">
<head>
<meta charset="UTF-8">
<title>NucleoMed – Cartão de Visita</title>
<link rel="stylesheet" href="https://fonts.googleapis.com/css2?family=Exo+2:wght@300;400&family=Open+Sans:wght@400;600&display=swap">
<style>
  :root {
    --page-bg: #e9e7e4;
    --navy: #2d5884;
    --navy-deep: #22466d;
    --sky: #4db3e8;
    --sky-soft: #8fd3f5;
    --lime: #8cc63f;
    --paper: #ffffff;
    --ink: #3b4a5a;
    --mist: #dfe7ef;
  }
  * { margin: 0; padding: 0; box-sizing: border-box; }
  html, body { width: 1200px; height: 1200px; overflow: hidden; }
  body {
    background: var(--page-bg);
    font-family: "Open Sans", sans-serif;
    position: relative;
  }
  .card {
    position: absolute;
    left: 150px;
    width: 900px;
    height: 500px;
    border-radius: 6px;
    overflow: hidden;
    box-shadow: 0 10px 30px rgba(0,0,0,.15);
  }

  /* Front */
  .card-front {
    top: 70px;
    background: linear-gradient(160deg, var(--navy) 0%, var(--navy-deep) 100%);
    color: var(--mist);
  }
  .card-front .edge-line {
    position: absolute; top: 0; bottom: 0; width: 4px; background: var(--paper); opacity: .85;
  }
  .card-front .edge-line.left { left: 22px; }
  .card-front .edge-line.right { right: 22px; }
  .front-mark {
    position: absolute; left: 50%; top: 70px; transform: translateX(-50%);
    width: 130px; height: 130px; border-radius: 50%;
    background: radial-gradient(circle at 40% 35%, var(--sky-soft), var(--sky));
  }
  .brand-name {
    font-family: "Exo 2", sans-serif;
    font-weight: 300;
    letter-spacing: 6px;
  }
  .card-front .brand-name {
    position: absolute; top: 222px; width: 100%; text-align: center;
    font-size: 64px; color: var(--mist);
  }
  .tagline {
    font-family: "Exo 2", sans-serif;
    font-weight: 300;
    letter-spacing: 3px;
    text-transform: uppercase;
  }
  .card-front .tagline {
    position: absolute; top: 306px; width: 100%; text-align: center;
    font-size: 20px; color: var(--mist);
  }
  .card-front .website {
    position: absolute; bottom: 48px; width: 100%; text-align: center;
    font-size: 20px; letter-spacing: 2px; color: var(--mist);
  }

  /* Back */
  .card-back {
    top: 630px;
    background: var(--paper);
    color: var(--ink);
  }
  .back-mark {
    position: absolute; left: 70px; top: 40px;
    width: 190px; height: 190px; border-radius: 50%;
    background: radial-gradient(circle at 40% 35%, var(--sky-soft), var(--sky));
  }
  .card-back .brand-block {
    position: absolute; right: 100px; top: 48px; text-align: right;
  }
  .card-back .brand-name { font-size: 40px; color: var(--sky); letter-spacing: 4px; }
  .card-back .tagline { font-size: 12px; color: var(--ink); margin-top: 2px; }
  .contact-list {
    position: absolute; right: 100px; top: 190px;
    list-style: none; text-align: right;
    font-size: 17px; line-height: 1.55;
  }
  .contact-list .group { margin-bottom: 18px; }
  .side-strip {
    position: absolute; right: 0; top: 0; bottom: 0; width: 60px;
    background: var(--navy);
  }
  .side-strip .accent { height: 110px; background: var(--lime); }
  .strip-icons {
    position: absolute; top: 170px; left: 0; width: 60px;
    display: flex; flex-direction: column; align-items: center; gap: 34px;
  }
  .strip-icons svg { width: 26px; height: 26px; }
</style>
</head>
<body>

  <section class="card card-front">
    <span class="edge-line left"></span>
    <span class="edge-line right"></span>
    <div class="front-mark"></div>
    <h1 class="brand-name">NUCLEOMED</h1>
    <p class="tagline">Prestadora de serviços em tecnologia</p>
    <p class="website">www.nucleomed.com.br</p>
  </section>

  <section class="card card-back">
    <div class="back-mark"></div>
    <div class="brand-block">
      <h2 class="brand-name">NUCLEOMED</h2>
      <p class="tagline">Prestadora de serviços em tecnologia</p>
    </div>
    <ul class="contact-list">
      <li class="group">(11) 0000-0000<br>(11) 0000-0001</li>
      <li class="group">contato@nucleomed.com.br<br>/nucleomed</li>
      <li>end. Rua dos Exemplos | Bairro<br>Cidade | Estado | CEP 00000-000</li>
    </ul>
    <div class="side-strip">
      <div class="accent"></div>
      <div class="strip-icons">
        <svg viewBox="0 0 24 24" aria-label="telefone"><path fill="#fff" d="M6.6 10.8a15.1 15.1 0 0 0 6.6 6.6l2.2-2.2a1 1 0 0 1 1-.25 11.4 11.4 0 0 0 3.6.57 1 1 0 0 1 1 1V20a1 1 0 0 1-1 1A17 17 0 0 1 3 4a1 1 0 0 1 1-1h3.5a1 1 0 0 1 1 1c0 1.25.2 2.45.57 3.57a1 1 0 0 1-.25 1z"/></svg>
        <svg viewBox="0 0 24 24" aria-label="rede social"><rect x="4" y="4" width="16" height="16" rx="2" fill="#fff"/></svg>
        <svg viewBox="0 0 24 24" aria-label="e-mail"><rect x="3" y="5" width="18" height="14" rx="1.5" fill="#fff"/><path d="M3.5 6l8.5 7 8.5-7" fill="none" stroke="#2d5884" stroke-width="1.6"/></svg>
        <svg viewBox="0 0 24 24" aria-label="endereço"><path fill="#fff" d="M12 2a7 7 0 0 0-7 7c0 5.2 7 13 7 13s7-7.8 7-13a7 7 0 0 0-7-7zm0 9.5A2.5 2.5 0 1 1 12 6.5a2.5 2.5 0 0 1 0 5z"/></svg>
      </div>
    </div>
  </section>

</body>
</html>
```